Generator Control - Superyacht Power Management System

We need a graphic design for a Touch Screen interface to control generators on Superyachts. We have a layout of the control system worked out, but need nice graphics to go with it.
The graphics comes down to a 300x460px App that i replicate several times on my 15" touchscreen as required.
See attached images.
The interface is divided up into 4 sections:
• Section#1 - 4 rectangles for the control
• Section#2 - a vertical bar graph,
• Section#3 - a section to display custom information
• Section#4 - a circuit breaker symbol.
The dimensions in pixels must be as per the attached image.
SECTION#1:
The 4 control rectangles correspond to 4 control modes:
• STOP – colours based on RED
• RUN – colours based on ORANGE
• RUN ONLINE – colours based on GREEN
• AUTO – colours based on BLUE
• THE TEXT DOESN’T HAVE TO BE ON THE GRAPHICS, WE JUST NEED THE BACKGROUND FOR THE TEXT, I ADD THE TEXT LATER USING SOFTWARE.
Each control rectangle needs to have 3 clearly identifiable states:
• Active/Selected (this is the currently active mode)
• Not Active/Not Selected (this mode is available but not currently active)
• Unavailable (this mode is not available)
SECTION#2:
The vertical bar graph design only needs the outline/frame of the bar graph. The actual moving part can be left blank; I will add that in later using an animation.
SECTION#3:
Free to look good as you want. See attached image for reference.
Within section#3 (at the top) is a 40x240px subsection, and should simply by 2 states, green or 'background colour of section#3 '. (green for when the generator is running, blend with the rest of section#3 when it is not). There are about 10 different texts I add on top of that square using software, corresponding to the status of the generator (starting, deloading, synchronizing, etc.)
SECTION#4:
Graphical representation of an electrical switch. Can be in two positions: opened or closed. See attached image as reference.

Target Market(s)

Cheif Engineers /Captains on Superyachts

Industry/Entity Type

Graphic Design

Requirements
Must have
• Must have the same graphics style as the uploaded file#2

```html
<!DOCTYPE html>
<html lang="en">
<head>
<meta charset="utf-8">
<title>Generator Control</title>
<link href="https://fonts.googleapis.com/css2?family=PT+Sans:wght@400;700&display=swap" rel="stylesheet">
<style>
:root{
  --bg:#000;
  --panel:#0c0c12;
  --panel-edge:#3a3d58;
  --bus:#2c3150;
  --node:#2c3150;
  --live:#4e6e2a;
  --frame:#8e8ad0;
  --frame-glow:rgba(140,130,255,.45);
  --text:#ffffff;
  --muted:#d8d8e0;
  --green-hi:#57ba8c; --green-lo:#1f9a4b;
  --orange-hi:#a8774d; --orange-lo:#9a4e04;
  --red-hi:#b9616a; --red-lo:#a72c33;
  --blue-hi:#4748b8; --blue-lo:#070794;
  --off:#444446; --off-text:#2c2c2e;
  --slot:#050505;
  --slot-lit:#5c7a32;
}
*{box-sizing:border-box;margin:0;padding:0}
html,body{width:1200px;height:789px;overflow:hidden;background:var(--bg)}
body{font-family:"PT Sans",sans-serif;color:var(--text)}
.canvas{position:relative;width:1200px;height:789px}
.busbar{position:absolute;left:0;top:0}
.generator{position:absolute;top:149px;width:480px;height:575px;background:var(--panel);
  border:2px solid var(--panel-edge);border-radius:6px;overflow:hidden}
.generator.port{left:79px}
.generator.starboard{left:638px}
.title-bar{position:absolute;left:0;top:0;width:100%;height:32px;background:#15151b;
  border-bottom:2px solid var(--panel-edge);display:flex;justify-content:space-between;align-items:center;font-size:17px}
.title-bar .name{padding-left:10px}
.title-bar .status{height:100%;display:flex;align-items:center;padding:0 8px 0 40px;
  background:linear-gradient(100deg,transparent 0,transparent 18px,#1c2a12 19px,#3b5a1d 100%)}
.mode{position:absolute;width:170px;height:103px;border-radius:7px;display:flex;flex-direction:column;
  justify-content:center;align-items:center;font-size:22px;line-height:1.15;text-align:center;border:2px solid transparent}
.mode.col-a{left:16px}.mode.col-b{left:199px}
.mode.row-a{top:58px}.mode.row-b{top:178px}
.mode.online{background:linear-gradient(var(--green-hi) 50%,var(--green-lo) 50%)}
.mode.run{background:linear-gradient(var(--orange-hi) 50%,var(--orange-lo) 50%)}
.mode.stop{background:linear-gradient(var(--red-hi) 50%,var(--red-lo) 50%)}
.mode.auto{background:linear-gradient(var(--blue-hi) 50%,var(--blue-lo) 50%)}
.mode.active{border-color:var(--frame);box-shadow:0 0 10px 2px var(--frame-glow)}
.mode.unavailable{background:var(--off);color:var(--off-text)}
.mode .sub{text-decoration:underline}
.readout{position:absolute;background:#000;border:2px solid var(--frame);border-radius:5px;
  box-shadow:0 0 6px var(--frame-glow);display:flex;align-items:center;justify-content:center}
.readout.large{left:16px;width:80px;height:48px;font-size:26px}
.readout.large.time{font-size:14px}
.readout.small{width:44px;height:48px;font-size:13px}
.label{position:absolute;font-size:16px;line-height:1.1;color:var(--muted)}
.label.big{left:104px}
.label.tiny{width:44px;text-align:center;font-size:13px}
.gauge-value{position:absolute;left:399px;width:66px;font-size:17px}
.gauge-value.pct{top:42px;height:42px}
.gauge-value.kw{top:521px;height:45px;flex-direction:column;font-size:15px;line-height:1}
.gauge{position:absolute;left:399px;top:91px;width:66px;height:412px;border-radius:6px;
  background:linear-gradient(90deg,#2a2a2e,#4a4a4e 40%,#d6d6d6 50%,#4a4a4e 60%,#2a2a2e);
  padding:14px 13px;display:flex;flex-direction:column;justify-content:space-between}
.slot{height:27px;border-radius:6px;background:var(--slot);border:1px solid #3a3a3a}
.slot.lit{background:linear-gradient(90deg,#3e5420,var(--slot-lit) 50%,#3e5420)}
.slot.half{background:linear-gradient(#050505 55%,#4d6a28 55%)}
</style>
</head>
<body>
<div class="canvas">
  <svg class="busbar" width="1200" height="160" viewBox="0 0 1200 160">
    <line x1="72" y1="55" x2="1120" y2="55" stroke="var(--bus)" stroke-width="5"/>
    <!-- port breaker: open -->
    <line x1="318" y1="55" x2="318" y2="74" stroke="var(--bus)" stroke-width="4"/>
    <line x1="286" y1="90" x2="318" y2="122" stroke="var(--live)" stroke-width="6"/>
    <line x1="318" y1="122" x2="318" y2="150" stroke="var(--bus)" stroke-width="4"/>
    <circle cx="318" cy="74" r="6" fill="var(--node)"/>
    <circle cx="318" cy="122" r="6" fill="var(--node)"/>
    <!-- starboard breaker: closed -->
    <line x1="879" y1="55" x2="879" y2="74" stroke="var(--bus)" stroke-width="4"/>
    <line x1="879" y1="74" x2="879" y2="122" stroke="var(--live)" stroke-width="6"/>
    <line x1="879" y1="122" x2="879" y2="150" stroke="var(--bus)" stroke-width="4"/>
    <circle cx="879" cy="74" r="6" fill="var(--node)"/>
    <circle cx="879" cy="122" r="6" fill="var(--node)"/>
  </svg>

  <section class="generator port">
    <header class="title-bar"><span class="name">Port Generator</span><span class="status">Status: Running Offline</span></header>
    <div class="mode online col-a row-a">Run<br>Online</div>
    <div class="mode run col-b row-a active">Run</div>
    <div class="mode stop col-a row-b">Stop</div>
    <div class="mode auto col-b row-b active">Automatic<span class="sub">1</span></div>

    <div class="readout large" style="top:305px">83</div><div class="label big" style="top:306px">Water<br>Temp.</div>
    <div class="readout large" style="top:372px">3.8</div><div class="label big" style="top:373px">Oil<br>Pres.</div>
    <div class="readout large" style="top:440px">1500</div><div class="label big" style="top:452px">RPM</div>
    <div class="readout large time" style="top:507px">00:03:33</div><div class="label big" style="top:508px">Online<br>Time</div>

    <div class="readout small" style="left:202px;top:305px">230</div><div class="label tiny" style="left:202px;top:355px">VAC</div>
    <div class="readout small" style="left:265px;top:305px">400</div><div class="label tiny" style="left:265px;top:355px">VAC</div>
    <div class="readout small" style="left:324px;top:305px">50.0</div><div class="label tiny" style="left:324px;top:355px">HZ</div>
    <div class="readout small" style="left:202px;top:401px">0</div><div class="label tiny" style="left:202px;top:451px">AL1</div>
    <div class="readout small" style="left:265px;top:401px">0</div><div class="label tiny" style="left:265px;top:451px">AL2</div>
    <div class="readout small" style="left:324px;top:401px">0</div><div class="label tiny" style="left:324px;top:451px">AL3</div>
    <div class="readout small" style="left:202px;top:494px">0</div><div class="label tiny" style="left:202px;top:544px">KVA</div>
    <div class="readout small" style="left:265px;top:494px">0.00</div><div class="label tiny" style="left:265px;top:544px">PF</div>

    <div class="readout gauge-value pct">0 %</div>
    <div class="gauge"><div class="slot"></div><div class="slot"></div><div class="slot"></div><div class="slot"></div><div class="slot"></div><div class="slot"></div><div class="slot"></div><div class="slot"></div><div class="slot"></div><div class="slot"></div><div class="slot"></div></div>
    <div class="readout gauge-value kw"><span>0</span><span>KW</span></div>
  </section>

  <section class="generator starboard">
    <header class="title-bar"><span class="name">Starboard Generator</span><span class="status">Status: Running Online</span></header>
    <div class="mode online col-a row-a active">Run<br>Online</div>
    <div class="mode run col-b row-a unavailable">Run</div>
    <div class="mode stop col-a row-b unavailable">Stop</div>
    <div class="mode auto col-b row-b">Automatic<span class="sub">_</span></div>

    <div class="readout large" style="top:305px">85</div><div class="label big" style="top:306px">Water<br>Temp.</div>
    <div class="readout large" style="top:372px">3.8</div><div class="label big" style="top:373px">Oil<br>Pres.</div>
    <div class="readout large" style="top:440px">1500</div><div class="label big" style="top:452px">RPM</div>
    <div class="readout large time" style="top:507px">00:03:33</div><div class="label big" style="top:508px">Online<br>Time</div>

    <div class="readout small" style="left:202px;top:305px">230</div><div class="label tiny" style="left:202px;top:355px">VAC</div>
    <div class="readout small" style="left:265px;top:305px">400</div><div class="label tiny" style="left:265px;top:355px">VAC</div>
    <div class="readout small" style="left:324px;top:305px">50.0</div><div class="label tiny" style="left:324px;top:355px">HZ</div>
    <div class="readout small" style="left:202px;top:401px">15</div><div class="label tiny" style="left:202px;top:451px">AL1</div>
    <div class="readout small" style="left:265px;top:401px">22</div><div class="label tiny" style="left:265px;top:451px">AL2</div>
    <div class="readout small" style="left:324px;top:401px">19</div><div class="label tiny" style="left:324px;top:451px">AL3</div>
    <div class="readout small" style="left:202px;top:494px">45</div><div class="label tiny" style="left:202px;top:544px">KVA</div>
    <div class="readout small" style="left:265px;top:494px">0.00</div><div class="label tiny" style="left:265px;top:544px">PF</div>

    <div class="readout gauge-value pct">63 %</div>
    <div class="gauge"><div class="slot"></div><div class="slot"></div><div class="slot"></div><div class="slot"></div><div class="slot"></div><div class="slot"></div><div class="slot half"></div><div class="slot lit"></div><div class="slot lit"></div><div class="slot lit"></div><div class="slot lit"></div></div>
    <div class="readout gauge-value kw"><span>41</span><span>KW</span></div>
  </section>
</div>
</body>
</html>
```